Agribusiness Insurance

I would like postcard designed to attract farmers and agribusiness owners to my insurance consulting services. My business model is being a Trusted Advisor through identifying exposures, developing strategies, implementing programs and then monitoring our designed plan. I am knowledge representative (13YRs ag insurance), Represent 15 Farm + Carriers (favorable pricing/competitive multiple options) Specialized in Confinements, Cattle Farms, and Grain Producers. No Membership Fees Necessary

Many Insurance Producers in my area are nearing retirement I am 33 and am looking to promote this..

Target Market(s)

Farmers and Agribusiness Owners

Industry/Entity Type

Agribusiness

Requirements
Must have

• Tobias Renholt
Phone: Cell 555 207 4163
Email: trenholt@plainsviewcover.example

```html
<!DOCTYPE html>
<html lang="en">
<head>
<meta charset="utf-8">
<title>Agricultural Insurance Postcard</title>
<link rel="stylesheet" href="https://fonts.googleapis.com/css2?family=Questrial&family=Oswald:wght@500&family=Roboto+Slab:wght@400;700&family=Lobster&display=swap">
<style>
  :root {
    --green: #8fb04b;
    --green-light: #a9c466;
    --green-dark: #4e6b2a;
    --red: #c4242c;
    --white: #ffffff;
    --ink: #1d1d1b;
  }
  html, body { margin: 0; padding: 0; overflow: hidden; background: var(--white); }
  .postcard { position: relative; width: 762px; height: 1200px; overflow: hidden; background: var(--white); }
  .face { position: absolute; left: 0; width: 762px; }
  .face--front { top: 0; height: 588px; }
  .face--back { top: 610px; height: 590px; background: linear-gradient(180deg, var(--green) 0%, var(--green-light) 60%, #b9cf7a 100%); }
  .face svg { position: absolute; left: 0; top: 0; }

  .tagline { position: absolute; left: 238px; top: 28px; margin: 0; font: 28px "Questrial", sans-serif; color: var(--ink); letter-spacing: .3px; }
  .tagline-rule { position: absolute; left: 230px; top: 68px; width: 532px; height: 3px; background: var(--ink); }

  .questions { position: absolute; right: 24px; top: 106px; text-align: right; font-family: "Oswald", sans-serif; color: var(--white); }
  .questions h2 { margin: 0 0 12px; font-size: 30px; font-weight: 500; letter-spacing: 1px; }
  .questions ul { list-style: none; margin: 0; padding: 0; }
  .questions li { font-size: 23px; line-height: 26px; margin-bottom: 12px; letter-spacing: .5px; }
  .questions li::before { content: "›"; display: inline-block; width: 14px; height: 14px; line-height: 12px; margin-right: 8px; border: 1.5px solid var(--white); border-radius: 50%; font-size: 14px; text-align: center; vertical-align: 4px; }

  .badge-text { position: absolute; text-align: center; font-family: "Roboto Slab", serif; }
  .badge-fees { left: 156px; top: 372px; width: 120px; color: var(--red); font-size: 16px; line-height: 20px; }
  .badge-fees strong { display: block; font-size: 20px; }
  .badge-years { left: 540px; top: 410px; width: 132px; color: var(--white); font-weight: 700; font-size: 16px; line-height: 22px; }
  .badge-years strong { display: block; font-size: 24px; line-height: 28px; }

  .contact { position: absolute; left: 210px; top: 432px; width: 380px; color: var(--white); font-family: "Roboto Slab", serif; }
  .contact-lead { margin: 0 0 0 80px; font-size: 18px; color: var(--ink); }
  .contact-name { margin: 4px 0 0 90px; font-size: 24px; font-weight: 700; letter-spacing: .5px; }
  .contact-phone { margin: 6px 0 0 90px; font-size: 22px; font-weight: 700; }
  .contact-email { margin: 10px 0 0 0; font-size: 18px; white-space: nowrap; }

  .back-title { position: absolute; left: 40px; top: 24px; margin: 0; font: 26px/34px "Roboto Slab", serif; color: var(--ink); letter-spacing: .5px; }
  .back-rule { position: absolute; left: 0; top: 94px; width: 360px; height: 3px; background: var(--ink); }
  .specialties { position: absolute; left: 28px; top: 120px; margin: 0; font: 25px/36px "Lobster", cursive; color: var(--white); }
  .offer { position: absolute; left: 196px; top: 258px; width: 124px; text-align: center; font: 700 16px/20px "Roboto Slab", serif; }
  .offer-price { color: var(--red); }
  .offer-divider { width: 18px; height: 2px; margin: 8px auto; background: var(--red); }
  .offer-options { color: var(--green-dark); }
</style>
</head>
<body>
<main class="postcard">
  <section class="face face--front">
    <svg width="762" height="588" viewBox="0 0 762 588" aria-hidden="false">
      <defs>
        <linearGradient id="fieldPhoto" x1="0" y1="0" x2="0" y2="1">
          <stop offset="0" stop-color="#b9c9d6"/>
          <stop offset=".45" stop-color="#c9b98a"/>
          <stop offset=".75" stop-color="#8a7a4a"/>
          <stop offset="1" stop-color="#5f6b3a"/>
        </linearGradient>
      </defs>
      <rect width="762" height="588" fill="var(--green)"/>
      <rect x="230" y="0" width="532" height="72" fill="var(--white)"/>
      <polygon points="0,0 236,0 470,588 0,588" fill="url(#fieldPhoto)" role="img" aria-label="Photo of a combine harvesting a corn field"/>
      <polygon points="236,72 286,72 762,548 762,598" fill="var(--white)"/>
      <polygon points="262,72 300,72 762,530 762,566" fill="var(--green-dark)"/>
      <circle cx="94" cy="60" r="94" fill="#6e9a3c" stroke="var(--white)" stroke-width="6" role="img" aria-label="Photo of a tractor spraying a green field"/>
      <polygon points="156,588 210,360 360,300 762,588" fill="var(--red)"/>
      <circle cx="382" cy="276" r="104" fill="#8a8076" stroke="var(--white)" stroke-width="6" role="img" aria-label="Portrait of the insurance representative"/>
      <circle cx="84" cy="494" r="66" fill="#b49a62" stroke="var(--white)" stroke-width="5" role="img" aria-label="Photo of a red tractor with a grain cart"/>
      <circle cx="216" cy="418" r="62" fill="var(--white)"/>
      <circle cx="606" cy="456" r="66" fill="var(--green-dark)" stroke="var(--white)" stroke-width="3"/>
    </svg>
    <h1 class="tagline">Experts in Agricultural Insurance</h1>
    <div class="tagline-rule"></div>
    <div class="questions">
      <h2>ARE YOU LOOKINF FOR:</h2>
      <ul>
        <li>A NEW FARM CARRIER?</li>
        <li>A KNOWLEDGEABLE<br>REPRESENTATIVE?</li>
        <li>LOWER PREMIUMS?</li>
        <li>MORE OPTIONS?</li>
        <li>BETTER SERVICE?</li>
      </ul>
    </div>
    <p class="badge-text badge-fees"><strong>No</strong>Membership<br>Fees<br>Necessary</p>
    <p class="badge-text badge-years"><strong>13+</strong>years<br>experience</p>
    <div class="contact">
      <p class="contact-lead">Inquiry, Please Contact</p>
      <p class="contact-name">TOBIAS RENHOLT</p>
      <p class="contact-phone">Tel: 555 207 4163</p>
      <p class="contact-email">Email: trenholt@plainsviewcover.example</p>
    </div>
  </section>

  <section class="face face--back">
    <svg width="762" height="590" viewBox="0 0 762 590">
      <defs>
        <linearGradient id="harvestPhoto" x1="0" y1="0" x2="1" y2="1">
          <stop offset="0" stop-color="#d8c07a" stop-opacity="0"/>
          <stop offset=".35" stop-color="#c86a3a"/>
          <stop offset=".7" stop-color="#d9b45a"/>
          <stop offset="1" stop-color="#b9cf7a" stop-opacity="0"/>
        </linearGradient>
      </defs>
      <rect x="0" y="200" width="440" height="390" fill="url(#harvestPhoto)" role="img" aria-label="Photo of a red combine harvesting wheat"/>
      <rect x="588" y="26" width="140" height="152" fill="none" stroke="#5a5a4a" stroke-width="2" stroke-dasharray="8 5"/>
      <g stroke="#6a7a4a" stroke-width="1.5">
        <line x1="380" y1="244" x2="728" y2="244"/>
        <line x1="380" y1="308" x2="728" y2="308"/>
        <line x1="380" y1="374" x2="728" y2="374"/>
        <line x1="380" y1="436" x2="728" y2="436"/>
      </g>
      <circle cx="258" cy="314" r="68" fill="var(--white)" stroke="var(--red)" stroke-width="4"/>
    </svg>
    <h2 class="back-title">TRUSTED INSURANCE<br>CONSULTING SERVICES</h2>
    <div class="back-rule"></div>
    <p class="specialties">Specialized in Confinements,<br>Cattle Farms, Grain Producers</p>
    <div class="offer">
      <div class="offer-price">FAVORABLE<br>PRICING</div>
      <div class="offer-divider"></div>
      <div class="offer-options">COMPETITIVE<br>MULTIPLE<br>OPTION</div>
    </div>
  </section>
</main>
</body>
</html>
```